business card for Franco-Turkish restaurant

We are a Franco-Turkish restaurant, Le Coquelicot, based in the Cotes d'Armor in Brittany, near the Pink Granite Coast. We serve mainly Turkish cuisine. We would like a card reminding Britain and Turkey. No flag. Color: turquoise (sea ..), green, red. There should be a space for 3 lines: name, address, phone / email

Industry/Entity Type

Fast Food Restaurant

Contact Information for Business Card

Dervan Oruzel
Addresse: 14 Rue Paul-Henri Dauvel, 22410 Kervalou, France
Tel:+33 2 96 47 83 09

Colors
33a6d7
f04a50
acd036

Nice to have
• Symbols of Britain and Turkey
Should not have
• No flags

```html
<!DOCTYPE html>
<html lang="en">
<head>
<meta charset="utf-8">
<title>Le Coquelicot — Business Card</title>
<link rel="stylesheet" href="https://fonts.googleapis.com/css2?family=Jost:wght@300;400&display=swap">
<style>
  :root {
    --backdrop: #e4e6ec;
    --slate-light: #4f7478;
    --slate-mid: #41605f;
    --slate-dark: #334a4b;
    --poppy-red: #c01d24;
    --poppy-red-dark: #a9171d;
    --sea-turquoise: #33a6d7;
    --meadow-green: #acd036;
    --ink-light: #f4f1f0;
    --ink-soft: #f6dcda;
  }
  * { box-sizing: border-box; margin: 0; padding: 0; }
  html, body {
    width: 1200px;
    height: 675px;
    overflow: hidden;
    background: var(--backdrop);
  }
  .canvas {
    width: 1200px;
    height: 675px;
    display: flex;
    align-items: center;
    justify-content: center;
  }
  .business-card {
    position: relative;
    width: 840px;
    height: 480px;
    overflow: hidden;
    background: radial-gradient(ellipse at 50% 38%, var(--slate-light) 0%, var(--slate-mid) 45%, var(--slate-dark) 100%);
    box-shadow: 0 12px 30px rgba(40, 50, 70, 0.18);
    font-family: "Jost", "Futura", sans-serif;
  }
  .brand {
    position: absolute;
    top: 150px;
    left: 0;
    right: 0;
    display: flex;
    align-items: center;
    justify-content: center;
    gap: 18px;
  }
  .brand-dot {
    width: 22px;
    height: 22px;
    border-radius: 50%;
    background: var(--poppy-red);
  }
  .brand-name {
    font-weight: 400;
    font-size: 58px;
    line-height: 1;
    letter-spacing: 1px;
    color: var(--ink-light);
  }
  .accent-stripes {
    position: absolute;
    left: 0;
    right: 0;
    bottom: 178px;
    height: 8px;
    display: flex;
    flex-direction: column;
  }
  .accent-stripes .stripe-turquoise { height: 4px; background: var(--sea-turquoise); }
  .accent-stripes .stripe-green { height: 4px; background: var(--meadow-green); }
  .contact-band {
    position: absolute;
    left: 0;
    right: 0;
    bottom: 0;
    height: 178px;
    background: linear-gradient(180deg, var(--poppy-red) 0%, var(--poppy-red-dark) 100%);
    box-shadow: 0 -3px 8px rgba(0, 0, 0, 0.25);
  }
  .contact-lines {
    position: absolute;
    top: 34px;
    left: 300px;
    right: 40px;
    list-style: none;
    font-weight: 300;
    font-size: 19px;
    line-height: 28px;
    letter-spacing: 0.3px;
    color: var(--ink-soft);
    white-space: nowrap;
  }
  .contact-name { font-weight: 400; color: var(--ink-light); }
</style>
</head>
<body>
  <main class="canvas">
    <section class="business-card" aria-label="Le Coquelicot business card">
      <div class="brand">
        <span class="brand-dot" aria-hidden="true"></span>
        <span class="brand-name">Le Coquelicot</span>
      </div>
      <div class="accent-stripes" aria-hidden="true">
        <span class="stripe-turquoise"></span>
        <span class="stripe-green"></span>
      </div>
      <div class="contact-band">
        <ul class="contact-lines">
          <li class="contact-name">Dervan Oruzel</li>
          <li>14 Rue Paul-Henri Dauvel, 22410 Kervalou</li>
          <li>Tel: +33 2 96 47 83 09 · contact@lecoquelicot.fr</li>
        </ul>
      </div>
    </section>
  </main>
</body>
</html>
```